Facebook Cover & Profile Branding for OlvendrA Technologies

We need a modern, premium Facebook cover image for our company Olvendra Technologies GmbH. The design should be clean, professional, and aligned with our corporate colors (neon green and deep blue) as well as our logo. It should clearly represent us as a technology and IT consulting company with a strong focus on software testing and quality assurance.

Since Olvendra Technologies is also active in the U.S. market, the design may include global or U.S.-related elements (e.g., subtle references to international presence, tech innovation with a global reach).

Requirements:

Integration of the Olvendra logo and brand colors

Modern, premium look with a tech-driven feel

Clear, simple layout that looks good on desktop and mobile

Optional: subtle U.S./international references to highlight our global presence

Goal:
A professional, eye-catching Facebook cover image that strengthens our brand identity and reflects our international expansion into the U.S. market.

Target Market(s)

Medium to large enterprises in the technology, finance, and energy sectors - Companies looking for premium IT consulting, software testing, and quality assurance services - Decision makers and executives (CIOs, CTOs, IT managers) in Europe and the United States - A global audience that values innovation, professionalism, and trust

Industry/Entity Type

Information Technology & Consulting Software Testing & Quality Assurance Technology / Professional Services Global IT Consulting with U.S. Market Presence

Requirements
Must have
• Integration of the Olvendra Technologies logo and brand colors (Neon Green & Deep Blue) Modern, premium design with a strong tech-oriented look and feel Clean and professional layout, optimized for both desktop and mobile display Clear visibility of the brand identity (technology, IT consulting, software testing, quality assurance) Subtle reference to U.S. presence / global expansion (to highlight activity in both Germany and the U.S.) Balanced use of colors and space for a high-end, corporate appearance
Nice to have
• Subtle animations or motion effects (e.g., light gradients, moving lines, glowing accents) Dark/Light version option for different moods or seasonal campaigns Integration of social media icons (LinkedIn, Instagram, Facebook) in a clean, minimal way Tech-inspired background elements (digital patterns, abstract shapes, network grids) Space for an optional tagline or slogan (e.g., “Innovation. Quality. Global Impact.”) Adaptability for other platforms (so the design style can be reused for LinkedIn or Twitter headers)
Should not have
• Cluttered or overloaded layouts that reduce clarity Low-quality stock photos or generic imagery that doesn’t fit a premium brand Use of colors outside the Olvendra brand identity (Neon Green & Deep Blue) Outdated design styles (e.g., heavy gradients, 3D effects, drop shadows) Complex text blocks that make the design look busy Elements that distract from the logo and core brand message Pop-art or playful styles that don’t match the premium, professional tech look

```html
<!DOCTYPE html>
<html lang="en">
<head>
<meta charset="UTF-8">
<title>Olvendra Technologies – Social Branding Set</title>
<link href="https://fonts.googleapis.com/css2?family=Outfit:wght@400;500;600&display=swap" rel="stylesheet">
<style>
  :root {
    --ink: #111418;
    --green: #2ecc4f;
    --neon: #1fe04a;
    --blue: #1467d6;
    --deep-blue: #0a3fa8;
    --paper: #f4f8fc;
    --paper-tint: #e6f1fb;
    --stage: #e4e7ea;
    --white: #ffffff;
    --photo-a: #c9d6e2;
    --photo-b: #8fa3b8;
  }
  * { box-sizing: border-box; margin: 0; padding: 0; }
  html, body { width: 1200px; height: 1200px; overflow: hidden; }
  body {
    background: var(--stage);
    font-family: "Outfit", sans-serif;
    color: var(--ink);
    position: relative;
  }
  .card { position: absolute; overflow: hidden; }

  .brand {
    position: absolute; display: flex; align-items: center; gap: 9px;
    font-weight: 600; color: var(--ink); white-space: nowrap; line-height: 1.05;
  }
  .brand-name span { display: block; }
  .brand-dot { border-radius: 50%; background: var(--green); flex: none; }

  .headline { position: absolute; font-weight: 500; line-height: 1.06; letter-spacing: -0.2px; }
  .headline span { display: block; }
  .headline .l-green { color: var(--green); }
  .headline .l-blue { color: var(--blue); }

  .contact-bar {
    position: absolute; left: 0; bottom: 0; display: flex; align-items: center;
    gap: 20px; color: var(--white); font-weight: 500;
  }
  .contact-item { display: flex; align-items: center; gap: 7px; white-space: nowrap; }
  .contact-item svg { flex: none; }
  .photo-layer { position: absolute; inset: 0; }

  /* Cover */
  .cover {
    left: 204px; top: 147px; width: 792px; height: 325px;
    background: linear-gradient(120deg, var(--paper-tint), var(--paper) 60%);
  }
  .cover .brand { left: 44px; top: 32px; font-size: 20px; }
  .cover .brand-dot { width: 30px; height: 30px; }
  .cover .headline { left: 44px; top: 102px; font-size: 35px; }
  .cover .tagline { position: absolute; left: 45px; top: 230px; font-size: 19px; }
  .cover .contact-bar {
    width: 520px; height: 43px; padding-left: 44px; font-size: 16px;
    background: linear-gradient(90deg, var(--blue), var(--green));
  }
  .cover .contact-item:first-child { font-size: 18px; }

  /* Square post */
  .post {
    left: 94px; top: 571px; width: 482px; height: 482px;
    background: linear-gradient(160deg, var(--paper-tint), var(--paper) 55%, var(--white));
  }
  .post .brand { left: 22px; top: 24px; font-size: 15px; }
  .post .brand-dot { width: 24px; height: 24px; }
  .post .headline { left: 22px; top: 261px; font-size: 31px; }
  .post .caption { position: absolute; left: 22px; top: 372px; font-size: 14px; text-transform: uppercase; }
  .post .body-copy { position: absolute; left: 22px; top: 400px; width: 320px; font-size: 9px; line-height: 1.4; color: #3a3f45; }
  .post .contact-bar {
    width: 482px; height: 36px; padding-left: 22px; font-size: 15px; gap: 24px;
    background: linear-gradient(90deg, #1aa88a, var(--green));
  }
  .post .contact-item:first-child { font-size: 17px; }

  /* Profile */
  .profile {
    left: 627px; top: 573px; width: 480px; height: 480px;
    background: linear-gradient(135deg, var(--deep-blue), #08876a 50%, #0aaa3a);
  }
  .profile .brand {
    left: 0; right: 0; top: 200px; justify-content: center; gap: 14px;
    font-size: 34px; color: var(--white);
  }
  .profile .brand-dot { width: 44px; height: 44px; background: var(--neon); }
</style>
</head>
<body>

<section class="card cover">
  <svg class="photo-layer" width="792" height="325" viewBox="0 0 792 325">
    <defs>
      <linearGradient id="cover-photo" x1="0" y1="0" x2="1" y2="1">
        <stop offset="0" stop-color="var(--photo-a)"/>
        <stop offset="1" stop-color="var(--photo-b)"/>
      </linearGradient>
      <linearGradient id="cover-edge" x1="0" y1="0" x2="0" y2="1">
        <stop offset="0" stop-color="var(--green)"/>
        <stop offset="1" stop-color="var(--blue)"/>
      </linearGradient>
    </defs>
    <path role="img" aria-label="Photo: businessman in glasses holding a tablet beside an office window"
      d="M362,0 C400,70 520,50 544,160 C556,230 488,250 500,325 L792,325 L792,0 Z" fill="url(#cover-photo)"/>
    <path d="M362,0 C400,70 520,50 544,160 C556,230 488,250 500,325" fill="none" stroke="url(#cover-edge)" stroke-width="6"/>
  </svg>
  <div class="brand"><span class="brand-dot"></span><span class="brand-name"><span>Olvendra</span><span>Technologies GmbH</span></span></div>
  <h1 class="headline">
    <span>EMPOWERING</span>
    <span class="l-green">TECHNOLOGY.</span>
    <span class="l-blue">ENABLING SUCCESS.</span>
  </h1>
  <p class="tagline">Excellent software quality. Globally minded.</p>
  <div class="contact-bar">
    <span class="contact-item">
      <svg width="16" height="16" viewBox="0 0 24 24" fill="currentColor"><path d="M6.6 10.8a15.1 15.1 0 0 0 6.6 6.6l2.2-2.2a1 1 0 0 1 1-.25 11.4 11.4 0 0 0 3.6.57 1 1 0 0 1 1 1V20a1 1 0 0 1-1 1A17 17 0 0 1 3 4a1 1 0 0 1 1-1h3.5a1 1 0 0 1 1 1c0 1.25.2 2.46.57 3.6a1 1 0 0 1-.25 1z"/></svg>
      00 07 412 630
    </span>
    <span class="contact-item">
      <svg width="18" height="13" viewBox="0 0 24 17" fill="none" stroke="currentColor" stroke-width="2"><rect x="1" y="1" width="22" height="15"/><path d="M1 1l11 9 11-9M1 16l8-7M23 16l-8-7"/></svg>
      admin@olvendratechnologies.com
    </span>
  </div>
</section>

<section class="card post">
  <svg class="photo-layer" width="482" height="482" viewBox="0 0 482 482">
    <defs>
      <linearGradient id="post-photo" x1="0" y1="0" x2="1" y2="1">
        <stop offset="0" stop-color="var(--photo-a)"/>
        <stop offset="1" stop-color="var(--photo-b)"/>
      </linearGradient>
    </defs>
    <path role="img" aria-label="Photo: businessman in glasses holding a tablet beside an office window"
      d="M215,0 C185,70 180,190 250,260 C315,322 410,335 482,305 L482,0 Z" fill="url(#post-photo)"/>
    <path d="M205,150 C210,200 225,235 256,262 C322,326 412,342 482,316" fill="none" stroke="var(--blue)" stroke-width="5"/>
  </svg>
  <div class="brand"><span class="brand-dot"></span><span class="brand-name"><span>Olvendra</span><span>Technologies GmbH</span></span></div>
  <h2 class="headline">
    <span>EMPOWERING</span>
    <span class="l-green">TECHNOLOGY.</span>
    <span class="l-blue">ENABLING SUCCESS.</span>
  </h2>
  <p class="caption">Excellent software quality. Globally minded.</p>
  <p class="body-copy">Neque porro quisquam est qui dolorem ipsum quia dolor sit amet, consectetur, adipisci velit</p>
  <div class="contact-bar">
    <span class="contact-item">
      <svg width="15" height="15" viewBox="0 0 24 24" fill="currentColor"><path d="M6.6 10.8a15.1 15.1 0 0 0 6.6 6.6l2.2-2.2a1 1 0 0 1 1-.25 11.4 11.4 0 0 0 3.6.57 1 1 0 0 1 1 1V20a1 1 0 0 1-1 1A17 17 0 0 1 3 4a1 1 0 0 1 1-1h3.5a1 1 0 0 1 1 1c0 1.25.2 2.46.57 3.6a1 1 0 0 1-.25 1z"/></svg>
      00 07 412 630
    </span>
    <span class="contact-item">
      <svg width="17" height="12" viewBox="0 0 24 17" fill="none" stroke="currentColor" stroke-width="2"><rect x="1" y="1" width="22" height="15"/><path d="M1 1l11 9 11-9M1 16l8-7M23 16l-8-7"/></svg>
      admin@olvendratechnologies.com
    </span>
  </div>
</section>

<section class="card profile" role="img" aria-label="Brand profile image: soft blue-to-green gradient background">
  <div class="brand"><span class="brand-dot"></span><span class="brand-name"><span>Olvendra</span><span>Technologies GmbH</span></span></div>
</section>

</body>
</html>
```